Election features for a political website

The Evening Lantern (www.eveninglantern.co.uk)
Web banner designs
Please have a look at The Evening Lantern website (www.eveninglantern.co.uk). We are seeking to add an advertising style banner at the top of every page and post. It will run right across the page (1024 pixels) and be in the region of 200 pixels vertically. (Please advise on what looks best size wise.
The banner will be a slider, operated in a similar way to the current homepage slider. There will be four items on the slider, and so we need four designs that match the aesthetic feel of the website. Each slider will link through to posts on the website.
1.
Headline: OUR CANDIDATE OF THE DAY
Space for a name, head and shoulders picture of the person to be dropped in and a one line reason. This will need to be in an editable format as this image will be changed each day for one month.
2.
Headline: HERO OF THE DAY
Space for name and a one line reason. This will need to be in an editable format as this image will be changed each day for one month.
3.
Headline: VILLAIN OF THE DAY
Space for name of the person to be dropped in and a one line reason. This will need to be in an editable format as this image will be changed each day for one month.
4.
Headline: TEL Poll – [Date]
If the election was today, who would you vote for?
Clickable options:
Harbourites
Meridan
Tallow Assembly
Pomo
Quill
Other
Can a poll widget be added to the banner? We would like this poll to reset each day and then pool the results into a graph day by day over a one month period.
Reason: Payment is now guaranteed. We would like to see more options.

```html
<!DOCTYPE html>
<html lang="en">
<head>
<meta charset="utf-8">
<title>The Evening Lantern – Election Banners</title>
<link rel="stylesheet" href="https://fonts.googleapis.com/css2?family=Cinzel:wght@600;700&family=Tinos:wght@400&display=swap">
<style>
  :root {
    --brand-blue: #0b5291;
    --panel: #f2f2f2;
    --body-text: #444444;
    --link: #0b3f73;
    --stage: #000000;
    --white: #ffffff;
    --photo-light: #e6e6e6;
    --photo-dark: #8a8a8a;
  }
  * { margin: 0; padding: 0; box-sizing: border-box; }
  html, body {
    width: 1200px; height: 1087px; overflow: hidden;
    background: var(--stage);
  }
  .banner-sheet { position: relative; width: 1200px; height: 1087px; }
  .banner {
    position: absolute; left: 67px; width: 1053px; height: 205px;
    background: var(--panel); overflow: hidden;
  }
  .banner--candidate { top: 33px; }
  .banner--hero { top: 290px; }
  .banner--villain { top: 568px; }
  .banner--poll { top: 836px; }
  .banner__shapes { position: absolute; inset: 0; width: 1053px; height: 205px; }
  .banner__headline {
    position: absolute; left: 36px; top: 0; height: 78px;
    display: flex; align-items: center; gap: 14px;
    font-family: "Cinzel", "Times New Roman", serif; font-weight: 700;
    font-size: 39px; letter-spacing: 1.5px; color: var(--white);
    white-space: nowrap;
  }
  .banner__icon { width: 42px; height: 42px; fill: var(--white); }
  .banner__reason {
    position: absolute; left: 37px; top: 96px; width: 600px;
    font-family: "Tinos", "Times New Roman", serif; font-size: 18.5px;
    line-height: 31px; color: var(--body-text);
  }
  .banner__link {
    position: absolute; left: 36px; top: 167px;
    font-family: "Tinos", "Times New Roman", serif; font-size: 17px;
    color: var(--link); text-decoration: underline; text-underline-offset: 3px;
  }
  .banner__name {
    position: absolute; right: 26px; top: 161px;
    font-family: "Tinos", "Times New Roman", serif; font-size: 28px;
    color: var(--white);
  }
  /* Poll */
  .poll__headline {
    position: absolute; left: 28px; top: 0; height: 63px;
    display: flex; align-items: center; gap: 14px;
    font-family: "Cinzel", "Times New Roman", serif; font-weight: 700;
    font-size: 30px; letter-spacing: 1px; color: var(--white); white-space: nowrap;
  }
  .poll__icon { width: 30px; height: 36px; }
  .poll__question {
    position: absolute; left: 29px; top: 76px;
    font-family: "Tinos", "Times New Roman", serif; font-size: 26px; color: #111;
  }
  .poll__option {
    position: absolute; display: flex; align-items: center; gap: 8px;
    font-family: "Tinos", "Times New Roman", serif; font-size: 20px; color: #111;
  }
  .poll__radio {
    width: 13px; height: 13px; border-radius: 50%;
    border: 1.6px solid #555; background: var(--white);
  }
  .poll__vote {
    position: absolute; left: 523px; top: 167px; width: 110px; height: 36px;
    display: flex; align-items: center; justify-content: center;
    font-family: "Tinos", "Times New Roman", serif; font-size: 20px; color: var(--white);
  }
</style>
</head>
<body>
<main class="banner-sheet">

  <!-- Candidate of the day -->
  <section class="banner banner--candidate">
    <svg class="banner__shapes" viewBox="0 0 1053 205" aria-hidden="true">
      <defs>
        <linearGradient id="portrait-tone" x1="0" y1="0" x2="1" y2="1">
          <stop offset="0" stop-color="#d9d9d9"/>
          <stop offset="0.5" stop-color="#a9a9a9"/>
          <stop offset="1" stop-color="#ececec"/>
        </linearGradient>
      </defs>
      <polygon points="0,0 678,0 656,78 0,78" fill="var(--brand-blue)"/>
      <polygon points="692,0 707,0 648,205 633,205" fill="var(--brand-blue)"/>
      <polygon points="707,0 1053,0 1053,205 648,205" fill="url(#portrait-tone)" role="img" aria-label="Black and white head and shoulders portrait of the candidate"/>
      <polygon points="844,155 1053,155 1053,205 827,205" fill="var(--brand-blue)"/>
    </svg>
    <h2 class="banner__headline">Our Candidate of the Day</h2>
    <p class="banner__reason">Reason: Lorem ipsum dolor sit amet, consectetur adipiscing elit, sed do eiusmod tempor incididunt ut labore et dolore magna aliqua.</p>
    <a class="banner__link" href="#">Read Full Story Here</a>
    <span class="banner__name">Clara Holt</span>
  </section>

  <!-- Hero of the day -->
  <section class="banner banner--hero">
    <svg class="banner__shapes" viewBox="0 0 1053 205" aria-hidden="true">
      <polygon points="0,0 678,0 656,78 0,78" fill="var(--brand-blue)"/>
      <polygon points="692,0 707,0 648,205 633,205" fill="var(--brand-blue)"/>
      <polygon points="707,0 1053,0 1053,205 648,205" fill="url(#portrait-tone)" role="img" aria-label="Black and white portrait of the hero of the day"/>
      <polygon points="844,155 1053,155 1053,205 827,205" fill="var(--brand-blue)"/>
    </svg>
    <h2 class="banner__headline">
      <svg class="banner__icon" viewBox="0 0 40 40" aria-hidden="true">
        <rect x="2" y="17" width="8" height="21" rx="1"/>
        <path d="M13 18 L20 4 C22 1 26 2 25 7 L23 15 L35 15 C38 15 39 18 38 20 C39 22 38 24 37 25 C38 27 37 29 35 30 C36 32 35 35 32 36 L16 37 C14 37 13 36 13 34 Z"/>
      </svg>
      Hero of the Day
    </h2>
    <p class="banner__reason">Reason: Lorem ipsum dolor sit amet, consectetur adipiscing elit, sed do eiusmod tempor incididunt ut labore et dolore magna aliqua.</p>
    <a class="banner__link" href="#">Read Full Story Here</a>
    <span class="banner__name">Clara Holt</span>
  </section>

  <!-- Villain of the day -->
  <section class="banner banner--villain">
    <svg class="banner__shapes" viewBox="0 0 1053 205" aria-hidden="true">
      <polygon points="0,0 678,0 656,78 0,78" fill="var(--brand-blue)"/>
      <polygon points="692,0 707,0 648,205 633,205" fill="var(--brand-blue)"/>
      <polygon points="707,0 1053,0 1053,205 648,205" fill="url(#portrait-tone)" role="img" aria-label="Black and white portrait of the villain of the day"/>
      <polygon points="844,155 1053,155 1053,205 827,205" fill="var(--brand-blue)"/>
    </svg>
    <h2 class="banner__headline">
      <svg class="banner__icon" viewBox="0 0 40 40" aria-hidden="true" style="transform: scaleY(-1)">
        <rect x="2" y="17" width="8" height="21" rx="1"/>
        <path d="M13 18 L20 4 C22 1 26 2 25 7 L23 15 L35 15 C38 15 39 18 38 20 C39 22 38 24 37 25 C38 27 37 29 35 30 C36 32 35 35 32 36 L16 37 C14 37 13 36 13 34 Z"/>
      </svg>
      Villain of the Day
    </h2>
    <p class="banner__reason">Reason: Lorem ipsum dolor sit amet, consectetur adipiscing elit, sed do eiusmod tempor incididunt ut labore et dolore magna aliqua.</p>
    <a class="banner__link" href="#">Read Full Story Here</a>
    <span class="banner__name">Clara Holt</span>
  </section>

  <!-- Daily poll -->
  <section class="banner banner--poll">
    <svg class="banner__shapes" viewBox="0 0 1053 205" aria-hidden="true">
      <defs>
        <linearGradient id="badge-tone" x1="0" y1="0" x2="1" y2="1">
          <stop offset="0" stop-color="#bdbdbd"/>
          <stop offset="0.5" stop-color="#7d7d7d"/>
          <stop offset="1" stop-color="#c9c9c9"/>
        </linearGradient>
      </defs>
      <polygon points="0,0 680,0 663,63 0,63" fill="var(--brand-blue)"/>
      <polygon points="689,0 704,0 646,205 631,205" fill="var(--brand-blue)"/>
      <polygon points="704,0 1053,0 1053,205 646,205" fill="url(#badge-tone)" role="img" aria-label="Pile of black and white vote campaign badges"/>
      <polygon points="529,166 633,166 625,202 519,202" fill="var(--brand-blue)"/>
    </svg>
    <h2 class="poll__headline">
      <svg class="poll__icon" viewBox="0 0 30 36" aria-hidden="true" fill="none" stroke="var(--white)" stroke-width="2.4">
        <path d="M10 22 L10 5 C10 3 12 2 14 3 L16 5 L16 22"/>
        <rect x="3" y="20" width="24" height="14" rx="1.5"/>
        <line x1="8" y1="20" x2="22" y2="20"/>
      </svg>
      TEL Poll –&nbsp; Mar 17 2015
    </h2>
    <p class="poll__question">If the election was today, who would you vote for?</p>
    <label class="poll__option" style="left:28px; top:122px"><span class="poll__radio"></span>Harbourites</label>
    <label class="poll__option" style="left:234px; top:122px"><span class="poll__radio"></span>Meridan</label>
    <label class="poll__option" style="left:384px; top:122px"><span class="poll__radio"></span>Tallow Assembly</label>
    <label class="poll__option" style="left:28px; top:161px"><span class="poll__radio"></span>Pomo</label>
    <label class="poll__option" style="left:234px; top:161px"><span class="poll__radio"></span>Quill</label>
    <label class="poll__option" style="left:384px; top:161px"><span class="poll__radio"></span>Other</label>
    <span class="poll__vote">Vote Now</span>
  </section>

</main>
</body>
</html>
```